Brightpath Dentistry - Flyer - Modern & Eye catching campaign flyer

Need front & back side full page flyer designs for both 1) Grand opening 2) On-going campaign.

Attached the new dental office logo.
Attached our other dental clinic flyer designs for content.

Target Market(s)

Cosmetic dentistry

Industry/Entity Type

Health Care

Requirements
Must have
• decent, modern and eye catching marketing flyers.
Nice to have
• - Nice space
• - Highlight phone number
• - Highlight special features like convenient hours, call or text, for all ages, digital facility, etc
Should not have
• - Don't want to fill the flyer with too much wordings
• - Too many colors

```html
<!DOCTYPE html>
<html lang="en">
<head>
<meta charset="utf-8">
<title>Brightpath Dentistry – Grand Opening Flyer</title>
<link rel="stylesheet" href="https://fonts.googleapis.com/css2?family=Archivo+Black&family=Oswald:wght@600&family=Roboto:wght@300;400;500;700;900&display=swap">
<style>
:root{
  --board:#d9dcdf;
  --label:#4a4a4a;
  --paper:#f7f6f4;
  --teal:#12b3d6;
  --teal-deep:#0aa3c8;
  --teal-light:#bfe6ee;
  --blue:#2b68b1;
  --navy:#6f84a3;
  --lavender:#a9bedf;
  --ink:#333;
  --white:#fff;
}
*{margin:0;padding:0;box-sizing:border-box}
html,body{width:1200px;height:879px;overflow:hidden}
body{background:linear-gradient(180deg,#e4e6e8,#cfd2d5);font-family:"Roboto",sans-serif;position:relative;color:var(--ink)}
.side-label{position:absolute;top:24px;width:562px;text-align:center;font-family:"Oswald",sans-serif;font-weight:600;font-size:22px;color:var(--label);letter-spacing:.5px}
.page{position:absolute;top:72px;width:563px;height:789px;background:var(--paper);overflow:hidden;box-shadow:0 2px 8px rgba(0,0,0,.25)}
.front{left:25px}
.back{left:613px}
.abs{position:absolute}
.brand{display:flex;align-items:center;gap:7px;font-weight:500;font-size:19px;letter-spacing:.3px}
.brand-dot{width:14px;height:14px;border-radius:50%}
/* front */
.hero-art{position:absolute;left:0;top:0;width:563px;height:560px}
.front .brand{left:355px;top:112px;color:var(--white)}
.front .brand .brand-dot{background:var(--white)}
.headline{position:absolute;left:272px;top:250px;width:240px;text-align:center;font-family:"Archivo Black",sans-serif;color:var(--white);line-height:1;text-shadow:2px 2px 0 var(--blue)}
.headline .l1,.headline .l2{display:block;font-size:41px}
.headline .l2{margin-top:2px}
.headline .l3{display:block;font-size:23px;margin-top:3px}
.offer-list{position:absolute;left:292px;top:384px;list-style:none;color:var(--white);font-weight:300;font-size:12.5px}
.offer-list li{display:flex;align-items:center;gap:9px;height:22.5px}
.tick{width:15px;height:15px;flex:none}
.fine-print{position:absolute;left:14px;top:408px;transform:rotate(28deg);transform-origin:left top;font-size:7.5px;font-style:italic;font-weight:300;color:var(--white);white-space:nowrap}
.hours{position:absolute;right:298px;top:572px;text-align:right;font-weight:900;font-size:15px;line-height:17px;color:var(--blue)}
.welcome{position:absolute;right:298px;top:612px;font-weight:900;font-size:15px;color:var(--teal);white-space:nowrap}
.divider{position:absolute;left:282px;top:567px;width:2px;height:62px;background:var(--blue)}
.cta-label{font-weight:500;color:var(--blue);font-size:10.5px;text-align:center}
.front .cta-label{position:absolute;left:300px;top:569px;width:245px}
.phone-pill{position:absolute;display:flex;align-items:center;background:var(--blue);border-radius:22px;color:var(--white);font-family:"Oswald",sans-serif;font-weight:600}
.phone-pill .phone-icon{width:38px;height:38px;border-radius:50%;background:var(--white);border:3px solid var(--teal);display:flex;align-items:center;justify-content:center;flex:none;margin-left:2px}
.front .phone-pill{left:300px;top:586px;width:243px;height:40px;font-size:27px;letter-spacing:1.5px}
.phone-pill .num{flex:1;text-align:center}
.services-title{position:absolute;left:27px;top:668px;width:508px;display:flex;align-items:center;gap:10px;color:var(--blue);font-size:11px}
.services-title::before,.services-title::after{content:"";flex:1;height:1px;background:#888}
.services{position:absolute;left:14px;top:698px;width:536px;display:flex;list-style:none}
.services li{width:59.5px;text-align:center;font-size:6.5px;line-height:8px;color:#444}
.services svg{display:block;margin:0 auto 7px;width:22px;height:24px}
/* back */
.back .brand{left:310px;top:38px;color:var(--teal)}
.back .brand .brand-dot{background:var(--teal)}
.intro-band{position:absolute;left:0;top:71px;width:563px;height:258px;background:var(--teal)}
.intro-photo{position:absolute;left:0;top:29px;width:330px;height:300px;background:linear-gradient(90deg,#c9d6d3 0%,#b6c7c3 55%,rgba(18,179,214,0) 100%)}
.intro-text{position:absolute;left:280px;top:93px;width:224px;text-align:center;color:var(--white)}
.intro-text h2{font-weight:700;font-size:16.5px;line-height:1;text-shadow:1px 1px 0 var(--blue)}
.intro-text h2 .big{display:block;font-size:23.5px;margin-top:7px}
.intro-text p{font-weight:300;font-size:12px;line-height:19.4px;margin-top:12px}
.intro-text .doctor{display:block;margin-top:12px;font-weight:500;font-size:15px;color:var(--blue);letter-spacing:-.3px}
.feature-band{position:absolute;left:0;top:329px;width:563px;height:197px;background:linear-gradient(90deg,#dcecef,var(--teal-light))}
.feature-title{position:absolute;left:30px;top:360px;width:240px;text-align:center;font-weight:700;font-size:20.5px;line-height:27px;color:var(--blue)}
.tool-photo{position:absolute;left:0;top:430px;width:210px;height:96px;background:linear-gradient(160deg,rgba(255,255,255,0) 20%,#9fb2bf 60%,#7d8c99 100%)}
.features{position:absolute;left:306px;top:357px;list-style:none}
.features li{display:flex;align-items:center;height:36px;font-size:10.4px;line-height:12.5px;color:#333}
.features svg{width:22px;height:22px;margin-right:16px;flex:none}
.coverage{position:absolute;left:0;top:526px;width:320px;height:263px}
.badge{position:absolute;left:67px;top:566px;width:152px;height:152px;border-radius:50%;background:radial-gradient(circle at 50% 40%,#fff,#e7ebf0);border:4px solid var(--teal);text-align:center;padding-top:22px;font-weight:900;color:var(--blue);font-size:18px;line-height:22px}
.back .cta-label{position:absolute;left:67px;top:686px;width:152px}
.back .phone-pill{left:41px;top:702px;width:203px;height:36px;font-size:23px;letter-spacing:1px;border:2px solid var(--white)}
.back .phone-pill .phone-icon{width:32px;height:32px}
.contact{position:absolute;right:33px;top:547px;text-align:right;font-size:10.3px;line-height:13.4px;color:#333}
.contact strong{font-weight:700}
.map{position:absolute;left:342px;top:616px;width:188px;height:123px;background:linear-gradient(135deg,#eceef0,#dfe3e6);border:1px solid #ccc}
</style>
</head>
<body>

<div class="side-label" style="left:25px">FRONT</div>
<div class="side-label" style="left:613px">BACK</div>

<!-- FRONT -->
<section class="page front">
  <svg class="hero-art" viewBox="0 0 563 560" role="img" aria-label="Photo of a smiling patient in a dental chair with a dental mirror, blended into teal">
    <defs>
      <linearGradient id="heroFill" x1="0" y1="0" x2="1" y2="1">
        <stop offset="0" stop-color="#c7e3ea"/>
        <stop offset=".45" stop-color="#6cc9e2"/>
        <stop offset="1" stop-color="#0fb0d6"/>
      </linearGradient>
    </defs>
    <path d="M0 0H563V398C500 440 420 478 300 478C180 478 90 420 0 338Z" fill="url(#heroFill)"/>
    <path d="M55 391C150 470 250 505 320 507C420 510 490 470 528 439C490 490 420 520 320 518C230 516 140 470 55 391Z" fill="var(--navy)"/>
  </svg>

  <div class="brand abs"><span class="brand-dot"></span>Brightpath Dentistry</div>

  <h1 class="headline"><span class="l1">GRAND</span><span class="l2">OPENING</span><span class="l3">SPECIALS</span></h1>

  <ul class="offer-list">
    <li><svg class="tick" viewBox="0 0 16 16"><circle cx="8" cy="8" r="8" fill="#8cc63f"/><path d="M4 8.3l2.6 2.6L12 5.4" stroke="#fff" stroke-width="1.8" fill="none"/></svg>Free Kids Dental Screening</li>
    <li><svg class="tick" viewBox="0 0 16 16"><circle cx="8" cy="8" r="8" fill="#8cc63f"/><path d="M4 8.3l2.6 2.6L12 5.4" stroke="#fff" stroke-width="1.8" fill="none"/></svg>$25 Adults Dental Screening</li>
    <li><svg class="tick" viewBox="0 0 16 16"><circle cx="8" cy="8" r="8" fill="#8cc63f"/><path d="M4 8.3l2.6 2.6L12 5.4" stroke="#fff" stroke-width="1.8" fill="none"/></svg>15% off on Treatment Plan</li>
  </ul>

  <p class="fine-print">Opening special offers valid until June 15, 2017 by Appointment only</p>

  <p class="hours">CONVENIENT EVENING<br>&amp; SATURDAY HOURS</p>
  <p class="welcome">NEW PATIENTS ARE WELCOME!</p>
  <div class="divider"></div>

  <p class="cta-label">Call or Text Us Now</p>
  <div class="phone-pill">
    <span class="phone-icon"><svg width="18" height="18" viewBox="0 0 20 20"><rect x="4" y="3" width="13" height="11" rx="2" fill="var(--blue)"/><path d="M7 7h7M7 10h7" stroke="#fff" stroke-width="1.3"/><path d="M6 14l-2 4 5-4z" fill="var(--blue)"/></svg></span>
    <span class="num">555.204.7810</span>
  </div>

  <h2 class="services-title">OUR SERVICES</h2>
  <ul class="services">
    <li><svg viewBox="0 0 22 24"><path d="M4 3c3-2 5 0 7 0s4-2 7 0c3 3 1 8 0 11l-2 8-3-7-2 0-3 7-2-8C2 11 1 6 4 3z" fill="none" stroke="var(--teal)" stroke-width="1.5"/></svg>Root Canal<br>Therapy</li>
    <li><svg viewBox="0 0 22 24"><path d="M2 10h18v6H2z" fill="none" stroke="var(--teal)" stroke-width="1.5"/><path d="M5 10v6M8 10v6M11 10v6M14 10v6M17 10v6" stroke="var(--teal)"/></svg>Dentures</li>
    <li><svg viewBox="0 0 22 24"><path d="M2 7h18v10H2z" fill="none" stroke="var(--teal)" stroke-width="1.5"/><path d="M2 12h18M8 7v10M14 7v10" stroke="var(--teal)"/></svg>Clear Aligners<br>(Invisible braces)</li>
    <li><svg viewBox="0 0 22 24"><path d="M5 5c3-2 4 0 6 0s3-2 6 0c2 3 1 7 0 9l-2 7-2-5h-4l-2 5-2-7C4 12 3 8 5 5z" fill="var(--teal)"/></svg>Laser Teeth<br>Whitening</li>
    <li><svg viewBox="0 0 22 24"><path d="M5 2c3-1 4 1 6 1s3-2 6-1c1 3 0 5-1 6H6C5 7 4 5 5 2z" fill="var(--teal)"/><path d="M8 10h6M8 13h6M9 16h4M10 19h2" stroke="var(--teal)" stroke-width="2"/></svg>Implants</li>
    <li><svg viewBox="0 0 22 24"><path d="M2 8c6 4 12 4 18 0v6c-6 4-12 4-18 0z" fill="none" stroke="var(--teal)" stroke-width="1.5"/></svg>Night Guards</li>
    <li><svg viewBox="0 0 22 24"><path d="M6 4c3-2 4 0 5 0s2-2 5 0c2 3 0 7-1 9l-2 6-2-4-2 4-2-6C5 11 4 7 6 4z" fill="none" stroke="var(--teal)" stroke-width="1.5"/><path d="M2 10c2 8 16 8 18 0" stroke="var(--teal)" stroke-width="1.5" fill="none"/></svg>Extractions</li>
    <li><svg viewBox="0 0 22 24"><path d="M3 8c3-3 13-3 16 0-3 6-13 6-16 0z" fill="none" stroke="var(--teal)" stroke-width="1.5"/><path d="M7 9v4M11 9v5M15 9v4" stroke="var(--teal)"/></svg>Veneers</li>
    <li><svg viewBox="0 0 22 24"><path d="M5 3c3-2 4 0 6 0s3-2 6 0c2 3 1 6 0 8H5C4 9 3 6 5 3z" fill="none" stroke="var(--teal)" stroke-width="1.5"/><path d="M8 13l-1 8M14 13l1 8M11 11v6" stroke="var(--teal)" stroke-width="1.5"/></svg>Crown and<br>Bridge</li>
  </ul>
</section>

<!-- BACK -->
<section class="page back">
  <div class="brand abs"><span class="brand-dot"></span>Brightpath Dentistry</div>

  <div class="intro-band"></div>
  <div class="intro-photo" role="img" aria-label="Photo of a dentist in a white coat standing with arms crossed in a clinic"></div>
  <div class="intro-text">
    <h2>LOOKING FOR DENTIST<span class="big">CLOSE TO HOME?</span></h2>
    <p>Come and See Us for Professional Services and Care. Our dentists and staff are experts in the field of advanced dentistry and will help you achieve your perfect smile.</p>
    <span class="doctor">Dr. Maren Colby, D.D.S.</span>
  </div>

  <div class="feature-band"></div>
  <h2 class="feature-title">FAMILY &amp; COSMETIC<br>DENTISTRY</h2>
  <div class="tool-photo" role="img" aria-label="Photo of a dental mirror and probe"></div>
  <ul class="features">
    <li><svg viewBox="0 0 22 22"><path d="M5 3v16M11 3v16M17 3v16" stroke="var(--teal)" stroke-width="1.5"/></svg>State-Of-The-Art equipment and<br>paperless facility.</li>
    <li><svg viewBox="0 0 22 22"><rect x="2" y="9" width="12" height="8" rx="3" fill="none" stroke="var(--teal)" stroke-width="1.3"/><rect x="14" y="4" width="6" height="13" rx="1" fill="none" stroke="var(--teal)" stroke-width="1.3"/></svg>Filled with entertainment devices<br>for patient comfort.</li>
    <li><svg viewBox="0 0 22 22"><rect x="3" y="4" width="16" height="15" fill="none" stroke="var(--teal)" stroke-width="1.3"/><path d="M3 8h16M7 11h2M11 11h2M15 11h2M7 15h2M11 15h2" stroke="var(--teal)"/></svg>Same-day appointment for<br>DENTAL EMERGENCIES</li>
    <li><svg viewBox="0 0 22 22"><circle cx="13" cy="11" r="5" fill="none" stroke="var(--teal)" stroke-width="1.3"/><path d="M16.5 14.5l4 4" stroke="var(--teal)" stroke-width="1.5"/><path d="M3 5c2-2 4 0 5 0s2-1 3 0" fill="none" stroke="var(--teal)" stroke-width="1.3"/></svg>Helping community with routine<br>free kids dental screening.</li>
  </ul>

  <svg class="coverage" viewBox="0 0 320 263" aria-hidden="true">
    <defs>
      <linearGradient id="coverFill" x1="0" y1="0" x2="1" y2="0">
        <stop offset="0" stop-color="#9fb6da"/>
        <stop offset="1" stop-color="#c3d2ea"/>
      </linearGradient>
    </defs>
    <path d="M0 0H245C300 60 310 170 250 263H0Z" fill="url(#coverFill)"/>
  </svg>
  <div class="badge">ALL<br>INSURANCES<br>ACCEPTED</div>
  <p class="cta-label">Call or Text Us Now</p>
  <div class="phone-pill">
    <span class="phone-icon"><svg width="16" height="16" viewBox="0 0 20 20"><rect x="4" y="3" width="13" height="11" rx="2" fill="var(--blue)"/><path d="M7 7h7M7 10h7" stroke="#fff" stroke-width="1.3"/><path d="M6 14l-2 4 5-4z" fill="var(--blue)"/></svg></span>
    <span class="num">555.204.7810</span>
  </div>

  <address class="contact" style="font-style:normal">
    <strong>Contact us:</strong><br>
    412 Linden Pike, Maple Hill PA 19000<br>
    www.BrightpathDental.com<br>
    hello@BrightpathDental.com
  </address>
  <div class="map" role="img" aria-label="Street map showing the office location"></div>
</section>

</body>
</html>
```